Home Page Design (+50 More Pages To Winning Designer!)

We have a 50+ page website, but we're starting with the home page. The winning designer will get all 50+ pages to design as a 2nd project, so make sure you do your best!

SoarVane is in the private jet industry and needs a re-designed website.

We have created the structure for the website and content inside of Tavoni.io (THESE ARE ONLY ROUGH A.I. GENERATED WIREFRAMES AND DO NOT NEED TO BE FOLLOWED EXACTLY) - https://www.tavoni.io/app/project/P482915_qRuVwKsLm-DDtaHrYuop72XNc8fkoPzqlrhwDxHkaWm3Tq

Take the content from the 'Home Page' under the 'Wireframe' tab on the Tavoni.io link above, but feel free to re-design the page in a better way as these are only A.I. generated wireframes.

We want a DARK theme.... High quality, luxurious feel, greyscale colors. Attached is a brand guideline (BUT THIS IS NOT A 100% BRAND GUIDELINE, YOU CAN CHANGE COLORS AND FONTS AND MAKE CHANGES IF YOU HAVE BETTER IDEAS) and attached is our logo. We are also attaching some examples of other apps and websites to give you a guideline of what we're looking for for this design project.

The final design MUST communicate luxury using high-quality imagery of large cabin luxurious private jets.

ENTRIES THAT DO NOT FOLLOW THE PROJECT BRIEF WILL BE AUTOMATICALLY DISCARDED. FOLLOW THE INSTRUCTIONS!

Industry/Entity Type

Travel

Number of Pages Required

1 page

Font styles to use
Sans Serif

Colors

Designer to choose colors to be used in the design.

Requirements
Must have
• Follow wireframe and use content in wireframe (see Tavoni.io link)

```html
<!DOCTYPE html>
<html lang="en">
<head>
<meta charset="utf-8">
<title>SoarVane — Luxury Private Jet Travel</title>
<link href="https://fonts.googleapis.com/css2?family=Manrope:wght@300;400;500;600&display=swap" rel="stylesheet">
<style>
:root{
  --bg:#000000;
  --panel:#2b2b2b;
  --band:#2e2e2e;
  --footer:#2f2f2f;
  --text:#ffffff;
  --muted:#b3b3b3;
  --line:#3a3a3a;
}
*{margin:0;padding:0;box-sizing:border-box}
html,body{width:1200px;height:3965px;overflow:hidden;background:var(--bg);color:var(--text);font-family:"Manrope",sans-serif}
.page{position:relative;width:1200px;height:3965px}
.abs{position:absolute}
h1,h2,h3{font-weight:500;letter-spacing:-0.01em}
p{color:var(--muted)}
.btn{position:absolute;display:flex;align-items:center;justify-content:center;gap:10px;font-size:15px;font-weight:500;color:var(--text);border:1.5px solid #d9d9d9}
.btn.solid{background:#fff;color:#000;border-color:#fff}
.photo{position:absolute}

.nav{position:absolute;top:0;left:0;width:1200px;height:70px;z-index:2}
.logo{position:absolute;display:flex;align-items:center;gap:6px;font-weight:400;color:var(--text)}
.logo .mark{width:12px;height:12px;background:#fff}
.nav-links{position:absolute;top:26px;left:589px;display:flex;gap:28px;font-size:14px}
.nav-links span{display:flex;align-items:center;gap:8px}

.hero{position:absolute;top:0;left:0;width:1200px;height:704px;background:linear-gradient(180deg,#0a0a0a 0%,#141414 35%,#3a2a1a 62%,#b8743a 72%,#3a2816 80%,#120d08 100%)}
.hero h1{position:absolute;left:50px;top:196px;font-size:36px;line-height:43px}
.hero p{position:absolute;left:50px;top:301px;font-size:16px;color:#e6e6e6}

.own h2{position:absolute;left:50px;top:758px;font-size:31px}
.own .lead{position:absolute;left:50px;top:814px;width:1100px;font-size:14.6px;line-height:21px;color:#e6e6e6}
.card{position:absolute;top:884px;height:180px;background:var(--panel);padding:20px 26px 20px 20px}
.card h3{font-size:20px;line-height:26px;margin-bottom:16px}
.card p{font-size:15px;line-height:24px}

.feat h2{position:absolute;left:50px;top:1134px;font-size:26px;line-height:32px;width:300px}
.feat .col{position:absolute;top:1136px;width:300px}
.feat .col h3{font-size:20px;margin-bottom:16px}
.feat .col p{font-size:15px;line-height:24px}

.rule{position:absolute;height:1px;background:var(--line)}
.ultimate{position:absolute;right:51px;top:1628px;text-align:right;font-size:26px;line-height:32px}

.services{position:absolute;top:1723px;left:0;width:1200px;height:200px;background:var(--band)}
.svc{position:absolute;top:34px;width:300px}
.svc h3{font-size:20px;line-height:26px;margin-bottom:14px}
.svc p{font-size:15px;line-height:24px}

.member h2{position:absolute;left:50px;top:2488px;font-size:26px}
.member p{position:absolute;left:50px;top:2535px;width:760px;font-size:15px;line-height:24px}

.quote .dash{position:absolute;left:371px;top:2700px;width:27px;height:1px;background:#888}
.quote h2{position:absolute;left:412px;top:2683px;font-size:26px}
.quote .text{position:absolute;left:371px;top:2737px;width:770px;font-size:15px;line-height:24px}
.quote .name{position:absolute;left:371px;top:2818px;font-size:26px;font-weight:500}
.quote .role{position:absolute;left:371px;top:2862px;font-size:14px}

.faq h2{position:absolute;left:50px;top:2950px;font-size:34px}
.faq .sub{position:absolute;left:50px;top:3012px;font-size:15px}
.q{position:absolute;left:50px;width:1100px;display:flex;justify-content:space-between;align-items:center;font-size:20px;font-weight:500}
.faq .ans{position:absolute;left:50px;top:3130px;width:1070px;font-size:15px;line-height:21px}

.cta h2{position:absolute;left:0;width:1200px;top:3432px;text-align:center;font-size:26px}

.footer{position:absolute;left:50px;top:3590px;width:1099px;height:266px;background:var(--footer)}
.footer .tag{position:absolute;left:48px;top:92px;font-size:15px;color:#d9d9d9}
.footer .copy{position:absolute;left:48px;top:126px;font-size:15px;color:#d9d9d9}
.fcol{position:absolute;top:50px;font-size:14px}
.fcol h4{font-weight:400;font-size:14px;margin-bottom:32px}
.fcol a{display:block;color:var(--muted);text-decoration:none;margin-bottom:19px}
.sub-note{font-size:14px;margin-bottom:14px}
.field{position:absolute;left:739px;top:140px;width:217px;height:32px;border:1px solid #8a8a8a;font-size:12px;color:#999;padding:8px 18px}
.subscribe{position:absolute;left:962px;top:140px;width:85px;height:32px;background:#fff;color:#000;font-size:12px;display:flex;align-items:center;justify-content:center}
.legal-note{position:absolute;left:739px;top:190px;width:300px;font-size:10px;line-height:15px;color:var(--muted)}

.follow{position:absolute;left:50px;top:3898px;font-size:19px;font-weight:500}
.social{position:absolute;top:3900px;display:flex;gap:22px;right:51px;font-size:14px;color:#e6e6e6}
</style>
</head>
<body>
<div class="page">

  <section class="hero">
    <div class="photo" style="inset:0" role="img" aria-label="Private jet parked on a runway at sunset"></div>
    <h1>Expreience the Ultimate<br>in Luxury Jet Travel</h1>
    <p>Discover the perfect flight program for you needs.</p>
    <span class="btn solid" style="left:50px;top:341px;width:99px;height:37px">Explore</span>
    <span class="btn" style="left:169px;top:341px;width:128px;height:37px">Learn more</span>
  </section>

  <header class="nav">
    <div class="logo" style="left:50px;top:22px;font-size:24px">SoarVane<span class="mark"></span></div>
    <nav class="nav-links">
      <span>Aircarft <svg width="10" height="6" viewBox="0 0 10 6"><path d="M1 1l4 4 4-4" stroke="#fff" stroke-width="1.5" fill="none"/></svg></span>
      <span>Programs</span>
      <span>Why SoarVane</span>
      <span>About us <svg width="10" height="6" viewBox="0 0 10 6"><path d="M1 1l4 4 4-4" stroke="#fff" stroke-width="1.5" fill="none"/></svg></span>
    </nav>
    <span class="btn solid" style="left:1027px;top:17px;width:122px;height:37px;font-size:14px">Inquiry Now</span>
  </header>

  <section class="own">
    <h2>Experience the Luxury of Fractional Jet&nbsp; Ownership</h2>
    <p class="lead">With SoarVane's fractional jet ownership program, you can enjoy the benefit&nbsp; of private jet travel without the hassle and expense of owning a whole aircraft. Our program offer flexibity, convenience, access to a fleet of luxurious jets, allowing you to travel in style&nbsp; an&nbsp; comfot</p>
    <div class="card" style="left:50px;width:358px"><h3>Flexibel ownership options avaiable</h3><p>Choose from a variety of ownership programs and enjoy the freedom to the fly you own terms</p></div>
    <div class="card" style="left:421px;width:357px"><h3>Convenient jet card programs</h3><p>Access a fleet of private jets with our exclusive jet card programs, offering, flexiblity and convenience</p></div>
    <div class="card" style="left:792px;width:357px"><h3>Flexibel lease programs</h3><p>Experience the luxury of private jet travel without the commitment with our flexible lease programs</p></div>
  </section>

  <section class="feat">
    <h2>Unparalleled Luxury and Convenience for Private Aviation</h2>
    <div class="col" style="left:415px"><h3>Convenience</h3><p>Enjoy hassle-free travel with our flexiible scheduling and personalized services</p></div>
    <div class="col" style="left:774px"><h3>Luxury</h3><p>Indulge in the lavish amenities and exquisite interiors of our private jets</p></div>
    <span class="btn" style="left:50px;top:1272px;width:156px;height:46px">Learn more <svg width="8" height="12" viewBox="0 0 8 12"><path d="M1.5 1.5l4.5 4.5-4.5 4.5" stroke="#fff" stroke-width="2" fill="none"/></svg></span>
    <div class="photo" style="left:258px;top:1272px;width:207px;height:316px;background:linear-gradient(180deg,#d8d4cc,#8a8378 60%,#3a342c)" role="img" aria-label="Jet cabin aisle with cream leather seats"></div>
    <div class="photo" style="left:478px;top:1272px;width:422px;height:316px;background:linear-gradient(135deg,#3a2a18,#a87a40 45%,#d9b070 70%,#6a4a28)" role="img" aria-label="Warm-lit jet cabin with leather armchairs and oval windows"></div>
    <div class="photo" style="left:912px;top:1272px;width:237px;height:316px;background:linear-gradient(180deg,#e6e3de,#a6a19a 60%,#4a4640)" role="img" aria-label="Bright jet cabin with white seating"></div>
  </section>

  <div class="rule" style="left:50px;top:1643px;width:748px"></div>
  <h2 class="ultimate">Exprience the Ultimate in<br>Private Jet Travel</h2>

  <section class="services">
    <div class="svc" style="left:77px"><h3>On demand Charter</h3><p>Fly anywhere, anytime with our on demand charter service</p></div>
    <div class="svc" style="left:448px"><h3>Global Medical Response<br>&amp; Recovery</h3><p>We provide specialized medical<br>transportation service wordwide.</p></div>
    <div class="svc" style="left:818px"><h3>Fractional Jet Ownership</h3><p>Enjoy the benefit of owning a private jet without the hassles</p></div>
  </section>

  <div class="photo" style="left:0;top:1923px;width:1200px;height:533px;background:linear-gradient(180deg,#cfcfcd 0%,#b9b9b6 45%,#7d7d7a 75%,#3d3d3b 100%)" role="img" aria-label="White private jet parked in front of a hangar"></div>
  <svg class="abs" style="left:580px;top:2227px" width="40" height="40" viewBox="0 0 40 40"><circle cx="20" cy="20" r="17" stroke="#fff" stroke-width="2.5" fill="none"/><path d="M16 13l11 7-11 7z" fill="none" stroke="#fff" stroke-width="2.5" stroke-linejoin="round"/></svg>

  <section class="member">
    <h2>Member Benefit - SoarVane</h2>
    <p>SoarVane is not simply a private jet service. Whether you're traveling for business or pleasure, Membership also delivers insider access to sports and cultural events, unique destinations, and travel experiences.</p>
    <span class="btn" style="left:915px;top:2513px;width:234px;height:46px">Learn more programs <svg width="8" height="12" viewBox="0 0 8 12"><path d="M1.5 1.5l4.5 4.5-4.5 4.5" stroke="#fff" stroke-width="2" fill="none"/></svg></span>
  </section>

  <section class="quote">
    <div class="photo" style="left:50px;top:2650px;width:279px;height:231px;background:linear-gradient(180deg,#6f7780,#9aa0a6 55%,#3a3c3f)" role="img" aria-label="Client standing beside a private jet on the tarmac"></div>
    <span class="dash"></span>
    <h2>What our client say about us</h2>
    <p class="text">Finding a private aviation company that would take care of airplane and help make sure that our personal needs were met was really important to us. We admire the SoarVane model</p>
    <div class="name">Mira Dalton</div>
    <p class="role">CMO, Lumen Analytics</p>
  </section>

  <section class="faq">
    <h2>Frequently Question</h2>
    <p class="sub">Find answer to commonn question about SoarVane's services and programs</p>
    <div class="rule" style="left:50px;top:3061px;width:1099px"></div>
    <div class="q" style="top:3094px"><span>What is SoarVane</span><svg width="14" height="8" viewBox="0 0 14 8"><path d="M1 7l6-6 6 6" stroke="#fff" stroke-width="2" fill="none"/></svg></div>
    <p class="ans">SoarVane&nbsp; is company that offers fractional jet ownership, jjet card program private jet lease program, all accsess programs, helicopter access program, and seat charter flights. We provide flexible and convenient options for individuals and businesses to access private aviation service</p>
    <div class="q" style="top:3198px"><span>How its works?</span><svg width="14" height="8" viewBox="0 0 14 8"><path d="M1 1l6 6 6-6" stroke="#fff" stroke-width="2" fill="none"/></svg></div>
    <div class="q" style="top:3252px"><span>Why choose SoarVane</span><svg width="14" height="8" viewBox="0 0 14 8"><path d="M1 1l6 6 6-6" stroke="#fff" stroke-width="2" fill="none"/></svg></div>
    <div class="q" style="top:3306px"><span>How to book?</span><svg width="14" height="8" viewBox="0 0 14 8"><path d="M1 1l6 6 6-6" stroke="#fff" stroke-width="2" fill="none"/></svg></div>
    <div class="rule" style="left:50px;top:3373px;width:1099px"></div>
  </section>

  <section class="cta">
    <h2>Exprience Luxury Travel Like Never Before</h2>
    <span class="btn solid" style="left:534px;top:3491px;width:130px;height:40px;font-size:16px">Inquiry Now</span>
  </section>

  <footer class="footer">
    <div class="logo" style="left:48px;top:42px;font-size:24px">SoarVane<span class="mark"></span></div>
    <p class="tag">Luxury and Convenience for Private Aviation</p>
    <p class="copy">Copyright © 2024</p>
    <div class="fcol" style="left:468px"><h4>Legal</h4><a>Privacy&nbsp; Notice</a><a>Cookie Notice</a></div>
    <div class="fcol" style="left:611px"><h4>About</h4><a>About us</a><a>Careers</a><a>Contact</a></div>
    <div class="fcol" style="left:739px"><h4>Subscribe</h4><div class="sub-note">Join our mailing list for the latest updates</div></div>
    <div class="field">Enter email adres</div>
    <div class="subscribe">Subsribe</div>
    <p class="legal-note">By subscribing you agree to our Privacy Policy and consent to receive updates</p>
  </footer>

  <div class="follow">Follow us</div>
  <div class="social"><span>Pictora</span><span>Workweb</span><span>Friendly</span></div>

</div>
</body>
</html>
```